Defense Attorney Business Card Design Project/ Stationary

I am looking for a distinctive business card design for my solo law practice.
I practice criminal defense, both juvenile and adult, including DUI. I am a very experienced attorney with prior military experience. The design should convey a traditional, old school flair, but not be too stodgy or uptight. Some color. My logo should appear.

Project Deadline Extended Reason: I misunderstood how this project works and I was not prepared with my logo when this project ran the first time. Added Thursday, November 13, 2014

Reason: I was sent overseas on military duty last year, which interrupted this project. Thank you for your participation... I hope we can get this done this week! Thank you, Des

Target Market(s)

Regular everyday people looking for strong, knowledgeable, authoritative representation while they are faced with criminal charges. Many have never been charged with a crime before. A reassuring air is therefore desired.

Industry/Entity Type

Business

Contact Information for Business Card

My information is:
Desmond R. Whitcombe, Attorney at Law
735 Linden Avenue Suite 300
Oakland, California 94618
Tel: (510) 555-0183
Fax: (510) 555-0162
email: deswhitcombelaw@mailbrook.net
web: www.deswhitcombelaw.net

Font styles to use
Serif
Sans Serif
Decorative

Colors
0255a3
ffffff

Requirements
Must have
• Sharp lines, bold elements. Conservative use of colors, such as deep blues, burgundy, grays for example.
• While my logo says "Des Whitcombe", it should be modified to show "Desmond R. Whitcombe".
Should not have
• Cliche imagery such as scales of justice, gavels, Tower of Varenholt, etc.

```html
<!DOCTYPE html>
<html lang="en">
<head>
<meta charset="utf-8">
<title>Des Whitcombe Law Firm – Business Card</title>
<link href="https://fonts.googleapis.com/css2?family=Open+Sans:wght@400;600&display=swap" rel="stylesheet">
<style>
  :root {
    --backdrop: #cfcfd1;
    --paper: #ffffff;
    --burgundy: #7d1a2b;
    --burgundy-soft: #9b2436;
    --graphite: #4b4b4e;
    --graphite-dark: #38383b;
    --graphite-light: #5d5d61;
    --rule-gray: #9a9a9e;
    --ink-light: #f2f2f2;
    --ink-muted: #d6d6d8;
  }
  * { box-sizing: border-box; margin: 0; padding: 0; }
  html, body {
    width: 1200px; height: 900px; overflow: hidden;
    background: var(--backdrop);
    font-family: "Open Sans", Arial, sans-serif;
  }
  .card-set {
    position: absolute; inset: 0;
    display: flex; align-items: center; justify-content: center; gap: 40px;
  }
  .card {
    position: relative;
    width: 530px; height: 303px;
    border-radius: 22px;
    overflow: hidden;
    box-shadow: 0 10px 24px rgba(0,0,0,0.25);
  }

  /* Front */
  .card--front { background: var(--paper); }
  .front-brand {
    position: absolute; left: 0; top: 0; width: 100%; height: 178px;
    display: flex; flex-direction: column; align-items: center; justify-content: center; gap: 14px;
  }
  .brand-mark { width: 46px; height: 46px; background: var(--burgundy); }
  .brand-name {
    color: var(--burgundy);
    font-weight: 600; font-size: 20px; letter-spacing: 1.5px;
    text-transform: uppercase;
  }
  .rule-burgundy { position: absolute; left: 0; top: 176px; width: 100%; height: 4px; background: var(--burgundy); }
  .rule-gray { position: absolute; left: 0; top: 183px; width: 100%; height: 3px; background: var(--rule-gray); }
  .texture-band {
    position: absolute; left: 0; top: 186px; width: 100%; height: 117px;
    background: linear-gradient(180deg, var(--graphite-light), var(--graphite) 55%, var(--graphite-dark));
  }
  .contact-block {
    position: absolute; left: 0; top: 186px; width: 100%; height: 117px;
    display: flex; padding-top: 12px;
  }
  .contact-person {
    width: 198px; text-align: right; padding-right: 14px;
  }
  .person-name { color: var(--burgundy-soft); font-size: 15px; line-height: 20px; }
  .person-title { color: var(--ink-light); font-size: 12px; line-height: 18px; }
  .contact-divider { width: 1px; height: 92px; background: var(--ink-muted); }
  .contact-details { padding-left: 14px; color: var(--ink-light); font-size: 13.5px; line-height: 17px; }
  .detail-row { display: flex; align-items: center; gap: 5px; }
  .detail-row svg { width: 12px; height: 12px; flex: none; fill: var(--burgundy-soft); }
  .detail-indent { padding-left: 17px; }
  .detail-gap { height: 14px; }

  /* Back */
  .card--back {
    background: radial-gradient(ellipse at 50% 45%, var(--graphite-light), var(--graphite) 60%, var(--graphite-dark));
    display: flex; flex-direction: column; align-items: center; justify-content: center; gap: 20px;
  }
  .card--back .brand-mark { width: 64px; height: 64px; }
  .card--back .brand-name { font-size: 24px; }
</style>
</head>
<body>
<main class="card-set">

  <section class="card card--front" aria-label="Business card front">
    <div class="front-brand">
      <div class="brand-mark"></div>
      <div class="brand-name">Des Whitcombe Law Firm</div>
    </div>
    <div class="rule-burgundy"></div>
    <div class="rule-gray"></div>
    <div class="texture-band" role="img" aria-label="Dark gray perforated metal texture"></div>
    <div class="contact-block">
      <div class="contact-person">
        <div class="person-name">Des Whitcombe</div>
        <div class="person-title">Director</div>
      </div>
      <div class="contact-divider"></div>
      <div class="contact-details">
        <div class="detail-row">
          <svg viewBox="0 0 12 12" aria-hidden="true"><path d="M6 1 L11.5 6 H10 V11 H7.2 V8 H4.8 V11 H2 V6 H0.5 Z"/></svg>
          <span>735 Linden Avenue Suite 300</span>
        </div>
        <div class="detail-indent">Oakland, California 94618</div>
        <div class="detail-gap"></div>
        <div class="detail-row">
          <svg viewBox="0 0 12 12" aria-hidden="true"><path d="M2.5 0.8 L4.6 0.8 L5.4 3.6 L4 4.6 C4.7 6.1 5.9 7.3 7.4 8 L8.4 6.6 L11.2 7.4 L11.2 9.5 C11.2 10.4 10.4 11.2 9.5 11.2 C4.9 11 1 7.1 0.8 2.5 C0.8 1.6 1.6 0.8 2.5 0.8 Z"/></svg>
          <span>(510) 555-0183</span>
        </div>
        <div class="detail-row">
          <svg viewBox="0 0 12 12" aria-hidden="true"><path d="M3 0.5 H9 V3.5 H3 Z M1 4.5 H11 V9.5 H9 V11.5 H3 V9.5 H1 Z M4 8 V10.5 H8 V8 Z"/></svg>
          <span>(510) 555-0162</span>
        </div>
        <div class="detail-row">
          <svg viewBox="0 0 12 12" aria-hidden="true"><path d="M0.5 2.5 H11.5 V9.5 H0.5 Z M1.2 3.2 L6 6.6 L10.8 3.2 Z" fill-rule="evenodd"/></svg>
          <span>deswhitcombelaw@mailbrook.net</span>
        </div>
      </div>
    </div>
  </section>

  <section class="card card--back" aria-label="Business card back">
    <div class="brand-mark"></div>
    <div class="brand-name">Des Whitcombe Law Firm</div>
  </section>

</main>
</body>
</html>
```